Website Design for my CNC machine Shop.

I need a new website for my Machining Company.

It can be a simple website that acts more like an "Online Business card" I has to highlight the services I provide and give Companies the confidence to engage my services.

I needs it to be a really modern or even a little futuristic promoting my Company.

I have just moved locations and have renovated the premises and would be great to let everyone know along with a new website.

If you can help with linking it to search engines to help get more exposure that would be great.

It needs to accommodate the three main services I provide which will include capacities of each machine (within that service) and maybe a couple images.
CNC Machining (5-axis, 3-axis)
EDM Wire cutting
3D Metal Printing
Along with home page and Contact page

I have two websites and you can use the txt from either/combination of these.
www.korvanmetalworks.com.au
(no longer do Laser Marking and etching but now do 3D metal Printing)
www.brislotech.com.au

Happy to chat further with the designer

Company logo's provided.

For Images: I am happy to use Pixelgrove and can purchase any images you like
EDM Wire cut
https://www.pixelgrove.com/search/edm-wire-cutting

CNC Machining:
https://www.pixelgrove.com/search/vertical-cnc-machining
Don't use any with engines or motor vehicle parts

3D metal Printing
https://www.pixelgrove.com/search/slm-metal-printing

Target Market(s)

Defence, Aerospace, Medical, HIgh Precision

Industry/Entity Type

Mechanical Engineering

Coding

Coded - Design and coding required

Number of Pages Required

5+ page

Requirements
Must have
• Home page, 3 services, Contacts. Can add image to each of the services

```html
<!DOCTYPE html>
<html lang="en">
<head>
<meta charset="utf-8">
<title>KORVAN Precision Machinists</title>
<link href="https://fonts.googleapis.com/css2?family=Poppins:wght@300;400;500;600;700;800&display=swap" rel="stylesheet">
<style>
:root{
  --green:#23905a;
  --green-dark:#1c7a4b;
  --ink:#141414;
  --text:#4a4a4a;
  --muted:#6d6d6d;
  --teal-deep:#123d46;
  --footer:#15414a;
  --line:#d6d6d6;
  --white:#ffffff;
}
*{box-sizing:border-box;margin:0;padding:0}
html,body{width:1200px;height:2880px;overflow:hidden}
body{font-family:'Poppins',sans-serif;color:var(--text);background:var(--white);position:relative}
a{color:inherit;text-decoration:none}
.abs{position:absolute}
.outline{color:transparent;-webkit-text-stroke:1.2px currentColor}

/* header */
.site-header{position:absolute;left:0;top:0;width:1200px;height:87px;background:var(--white)}
.brand{position:absolute;left:131px;top:14px}
.brand-name{font-weight:700;font-size:44px;letter-spacing:3px;color:#4e5c62;line-height:44px;display:flex;align-items:center;gap:8px}
.brand-name .dot{width:10px;height:10px;background:var(--green)}
.brand-tag{font-size:10.5px;letter-spacing:3px;color:var(--green);margin-top:3px}
.topbar{position:absolute;left:398px;top:0;width:802px;height:24px;background:var(--green);clip-path:polygon(12px 0,100% 0,100% 100%,0 100%);color:#fff;font-size:10px;display:flex;align-items:center}
.topbar .item{display:flex;align-items:center;gap:8px}
.topbar .sep{width:1px;height:12px;background:rgba(255,255,255,.6);margin:0 32px}
.socials{position:absolute;right:134px;top:6px;display:flex;gap:6px}
.socials span{width:12px;height:12px;border-radius:50%;background:rgba(255,255,255,.8)}
.main-nav{position:absolute;left:426px;top:48px;display:flex;align-items:center;font-size:10px;color:#222}
.main-nav a{padding:0 15px;border-left:1px solid #ccc;line-height:11px}
.main-nav a:first-child{border-left:0;padding-left:0;color:var(--green)}
.btn{display:inline-flex;align-items:center;justify-content:center;font-weight:500;font-size:11.5px;color:#fff;background:var(--green);clip-path:polygon(10px 0,100% 0,calc(100% - 10px) 100%,0 100%)}
.nav-cta{position:absolute;left:953px;top:40px;width:116px;height:33px}

/* hero */
.hero{position:absolute;left:0;top:87px;width:1200px;height:516px;background:linear-gradient(100deg,#163a48 0%,#224e62 40%,#4f7a90 70%,#2f5366 100%)}
.hero-eyebrow{left:131px;top:100px;font-size:12px;color:#3fb37a}
.hero-title{left:130px;top:120px;font-weight:800;font-size:47px;line-height:52px;color:#fff}
.hero-title .outline{-webkit-text-stroke:1.4px #fff;font-weight:700}
.hero-lead{left:131px;top:288px;width:330px;font-size:11px;line-height:17px;color:#fff}
.hero-actions{left:133px;top:343px;display:flex;gap:8px}
.hero-actions .btn{width:118px;height:32px}
.btn-ghost{background:transparent;position:relative;width:118px;height:32px;color:#fff;font-size:11.5px;display:flex;align-items:center;justify-content:center}
.btn-ghost svg{position:absolute;inset:0}
.hero-arrow{top:195px}

/* services */
.service{position:absolute;top:603px;height:299px;color:#fff}
.service h3{font-weight:600;font-size:21px}
.service p{font-size:16px;line-height:19px;font-weight:300;margin-top:10px}
.service .more{font-size:11px;font-weight:500;margin-top:20px;display:block}
.svc-cnc{left:0;width:461px;background:linear-gradient(120deg,#1a2a31,#2f3f46 60%,#1c2a30)}
.svc-edm{left:461px;width:278px;top:548px;height:354px;background:var(--green);clip-path:polygon(0 54px,50% 0,100% 54px,100% 100%,0 100%)}
.svc-print{left:739px;width:461px;background:linear-gradient(120deg,#1f2220,#3a3a32 55%,#6a5a3a 75%,#222)}

/* about */
.about-word{left:146px;top:1002px;writing-mode:vertical-rl;white-space:nowrap;font-weight:700;font-size:80px;line-height:80px;letter-spacing:1px;color:transparent;-webkit-text-stroke:1.5px #d2d2d2}
.about-visual{left:256px;top:1012px;width:226px;height:396px;background:linear-gradient(160deg,#8e9aa0 0%,#c9d0d3 45%,#7d8a90 100%)}
.years{left:362px;top:1274px;width:129px;height:125px;background:var(--green);color:#fff;text-align:center;padding-top:28px}
.years b{font-size:40px;font-weight:400;line-height:42px;display:block}
.years span{font-size:10px}
.eyebrow{font-size:13px;color:var(--green)}
.about-copy{left:608px;top:1012px;width:420px}
.sec-title{font-weight:700;font-size:33px;line-height:39px;color:var(--ink)}
.sec-title .outline{font-weight:500;-webkit-text-stroke:1.2px #555}
.about-copy p{font-size:12px;line-height:18.5px;margin-top:12px;color:#555}
.stats{left:612px;top:1245px;display:grid;grid-template-columns:208px 208px;row-gap:16px}
.stat{display:flex;align-items:center;gap:16px}
.stat b{font-size:21px;font-weight:600;color:var(--ink)}
.stat b i{font-style:normal;color:var(--green)}
.stat small{display:block;font-size:11px;color:var(--muted);line-height:15px}

/* location band */
.location{position:absolute;left:0;top:1526px;width:1200px;height:387px;background:linear-gradient(100deg,#1f8a57 0%,#2a8d62 45%,#497a5a 70%,#8a5a2e 85%,#2d2218 100%)}
.location .eyebrow{left:180px;top:96px;color:#fff;font-size:12px}
.location h2{left:180px;top:112px;font-weight:700;font-size:33px;line-height:38px;color:#fff}
.location h2 .outline{-webkit-text-stroke:1.2px #fff;font-weight:500}
.location p{left:181px;top:196px;width:420px;font-size:11px;line-height:17px;color:#fff}

/* contact */
.contact-head{left:0;top:1990px;width:1200px;text-align:center}
.contact-head .sec-title{font-size:34px;line-height:40px;margin-top:6px}
.dark-band{position:absolute;left:0;top:2435px;width:1200px;height:445px;background:var(--footer)}
.contact-photo{left:227px;top:2134px;width:376px;height:412px;background:radial-gradient(circle at 56% 68%,#f4c08a 0%,#b66a34 18%,#3a3a3a 45%,#9a9490 100%)}
.form-card{left:566px;top:2164px;width:412px;height:335px;background:#fff;box-shadow:0 6px 22px rgba(0,0,0,.08);padding:26px 22px}
.form-card h3{font-weight:500;font-size:19px;color:var(--ink)}
.fields{display:grid;grid-template-columns:173px 173px;gap:12px 10px;margin-top:20px}
.field{height:35px;border:1px solid var(--line);font-size:9.5px;color:#999;padding:11px 15px}
.field.msg{grid-column:1/3;height:88px}
.form-card .btn{width:120px;height:32px;margin-top:18px;margin-left:3px}

/* footer */
.footer-brand{left:178px;top:2640px}
.footer-brand .brand-name{font-size:33px;color:#d0d6d8;line-height:34px}
.footer-brand .brand-tag{font-size:8.5px;letter-spacing:2.4px;color:#3fb37a}
.footer-brand p{font-size:10.5px;line-height:16px;color:#fff;margin-top:18px;width:215px}
.f-social{display:flex;gap:7px;margin-top:22px}
.f-social span{width:25px;height:25px;border-radius:50%;background:rgba(255,255,255,.25)}
.f-col{top:2645px;color:#fff}
.f-col h4{font-weight:500;font-size:14px}
.f-col h4::after{content:"";display:block;width:17px;height:2px;background:var(--green);margin-top:8px}
.f-col ul{list-style:none;margin-top:12px;font-size:10px;line-height:19px}
.f-col li::before{content:"»";color:var(--green);margin-right:6px}
.f-contact li{display:flex;gap:10px;margin-bottom:11px;line-height:14px}
.f-contact li::before{content:none}
.copyright{left:0;top:2825px;width:1200px;text-align:center;font-size:10.5px;color:#fff}
</style>
</head>
<body>

<header class="site-header">
  <a class="brand" href="#">
    <div class="brand-name">KORVAN <span class="dot"></span></div>
    <div class="brand-tag">PRECISION MACHINISTS</div>
  </a>
  <div class="topbar">
    <div class="item" style="margin-left:58px">
      <svg width="10" height="10" viewBox="0 0 24 24" fill="#fff"><path d="M6.6 10.8a15.1 15.1 0 0 0 6.6 6.6l2.2-2.2a1 1 0 0 1 1-.25 11.4 11.4 0 0 0 3.6.57 1 1 0 0 1 1 1V20a1 1 0 0 1-1 1A17 17 0 0 1 3 4a1 1 0 0 1 1-1h3.5a1 1 0 0 1 1 1c0 1.25.2 2.45.57 3.57a1 1 0 0 1-.25 1z"/></svg>
      1.800.555.0147
    </div>
    <span class="sep"></span>
    <div class="item">
      <svg width="11" height="9" viewBox="0 0 24 18" fill="#fff"><path d="M0 0h24v18H0z" opacity=".95"/><path d="M0 0l12 9 12-9" stroke="#23905a" stroke-width="2" fill="none"/></svg>
      info@korvansupport.com
    </div>
    <div class="socials"><span></span><span></span><span></span><span></span></div>
  </div>
  <nav class="main-nav">
    <a href="#">HOME</a>
    <a href="#">ABOUT US</a>
    <a href="#">EDM WIRE CUTTING</a>
    <a href="#">CNC MACHINING</a>
    <a href="#">LASER MARKING AND ETCHING</a>
  </nav>
  <a class="btn nav-cta" href="#">Contact Us</a>
</header>

<section class="hero" role="img" aria-label="Close-up of a CNC machine spindle cutting a metal part with coolant spray, in cool blue tones">
  <svg class="abs hero-arrow" style="left:58px" width="14" height="28" viewBox="0 0 14 28"><path d="M12 2L2 14l10 12" stroke="#fff" stroke-width="1.5" fill="none"/></svg>
  <svg class="abs hero-arrow" style="left:1142px" width="14" height="28" viewBox="0 0 14 28"><path d="M2 2l10 12L2 26" stroke="#fff" stroke-width="1.5" fill="none"/></svg>
  <div class="abs hero-eyebrow">Welcome To Korvan Precision</div>
  <h1 class="abs hero-title">PRECISION<br>ENGINEERING FOR<br><span class="outline">THE FUTURE</span></h1>
  <p class="abs hero-lead">Leading Experts in CNC Machining, EDM Wire Cutting, and 3D Metal Printing.</p>
  <div class="abs hero-actions">
    <a class="btn" href="#">Learn More</a>
    <a class="btn-ghost" href="#"><svg width="118" height="32"><polygon points="10.5,0.5 117.5,0.5 107.5,31.5 0.5,31.5" fill="none" stroke="#fff"/></svg><span style="position:relative">Contact Us</span></a>
  </div>
</section>

<article class="service svc-cnc" role="img" aria-label="Dark photo of a vertical CNC machining centre">
  <div class="abs" style="left:132px;top:100px;width:260px">
    <h3>CNC Machining</h3>
    <p>Precision 5-axis and 3-axis CNC machining for complex.</p>
    <a class="more" href="#">Learn More</a>
  </div>
</article>
<article class="service svc-edm">
  <svg class="abs" style="left:42px;top:86px" width="46" height="54" viewBox="0 0 46 54" fill="none" stroke="#fff" stroke-width="1.6">
    <rect x="4" y="2" width="38" height="7"/><rect x="8" y="9" width="30" height="10"/>
    <circle cx="15" cy="14" r="2"/><circle cx="23" cy="14" r="2"/><circle cx="31" cy="14" r="2"/>
    <path d="M19 19h8v8h-8zM23 27v9M16 32l-4-2M30 32l4-2M17 38l-5 2M29 38l5 2"/>
    <path d="M6 44h34v4H6zM2 52h42"/>
  </svg>
  <div class="abs" style="left:42px;top:160px;width:210px">
    <h3>EDM Wire Cutting</h3>
    <p>Expert EDM wire cutting services for intricate and delicate components.</p>
    <a class="more" href="#">Learn More</a>
  </div>
</article>
<article class="service svc-print" role="img" aria-label="Metal 3D printer laser sintering a part with glowing sparks">
  <div class="abs" style="left:62px;top:100px;width:270px">
    <h3>3D Metal Printing</h3>
    <p>Advanced 3D metal printing for rapid prototyping and production of complex metal parts.</p>
    <a class="more" href="#">Learn More</a>
  </div>
</article>

<section aria-label="About">
  <div class="abs about-word" aria-hidden="true">ABOUT US</div>
  <div class="abs about-visual" role="img" aria-label="Photo of the machine shop floor shown inside a large letter-shaped frame"></div>
  <div class="abs years"><b>25</b><span>Years of experience</span></div>

  <div class="abs about-copy">
    <div class="eyebrow">About Us</div>
    <h2 class="sec-title" style="margin-top:8px">INTRODUCTION OF<br><span class="outline">COMPANY</span></h2>
    <p>At KORVAN, we are dedicated to providing top-tier precision engineering services to meet the demands of the most challenging industries. With over 25 years of experience, we specialize in CNC machining, EDM wire cutting, and 3D metal printing, ensuring the highest quality and precision for every project.</p>
  </div>

  <div class="abs stats">
    <div class="stat">
      <svg width="58" height="58" viewBox="0 0 58 58"><rect x="12" y="12" width="34" height="34" transform="rotate(45 29 29)" fill="none" stroke="#333"/><rect x="21" y="22" width="16" height="14" fill="none" stroke="#23905a" stroke-width="2"/><path d="M24 27h10M24 31h10" stroke="#222" stroke-width="2"/></svg>
      <div><b>150<i>+</i></b><small>PROJECTS</small></div>
    </div>
    <div class="stat">
      <svg width="58" height="58" viewBox="0 0 58 58"><rect x="12" y="12" width="34" height="34" transform="rotate(45 29 29)" fill="none" stroke="#333"/><circle cx="29" cy="23" r="4" fill="#222"/><path d="M21 34a8 6 0 0 1 16 0z" fill="#222"/><path d="M22 38h3M27.5 38h3M33 38h3" stroke="#23905a" stroke-width="2"/></svg>
      <div><b>100<i>+</i></b><small>SATISFIED CLIENTS</small></div>
    </div>
    <div class="stat">
      <svg width="58" height="58" viewBox="0 0 58 58"><rect x="12" y="12" width="34" height="34" transform="rotate(45 29 29)" fill="none" stroke="#333"/><path d="M36 21l-10 4-5 6 6 6 6-5 4-10z" fill="#222"/><circle cx="31" cy="27" r="2" fill="#fff"/><path d="M22 36l-3 3" stroke="#23905a" stroke-width="2"/></svg>
      <div><b>90<i>+</i></b><small>ONGOING<br>PROJECTS</small></div>
    </div>
    <div class="stat">
      <svg width="58" height="58" viewBox="0 0 58 58"><rect x="12" y="12" width="34" height="34" transform="rotate(45 29 29)" fill="none" stroke="#333"/><path d="M22 28h4v10h-4zM26 37h9l2-8h-6l1-6-3-1-3 6" fill="none" stroke="#222" stroke-width="1.8"/></svg>
      <div><b>25<i>+</i></b><small>YEAR OF<br>EXPERIENCE</small></div>
    </div>
  </div>
</section>

<section class="location" role="img" aria-label="Laser cutting head throwing bright sparks over a green-toned workshop">
  <div class="abs eyebrow">Renovations &amp; New Location</div>
  <h2 class="abs">NEW LOCATION AND STATE<br>OF-THE <span class="outline">ART FACILITIES</span></h2>
  <p class="abs">We are excited to announce that our company has moved to a new, larger facility New Address. This new location allows us to expand our capabilities and better serve our clients with the most advanced technology available.</p>
</section>

<div class="dark-band"></div>

<section aria-label="Contact">
  <div class="abs contact-head">
    <div class="eyebrow">Get In Touch</div>
    <h2 class="sec-title">READY TO START YOUR NEXT<br><span class="outline">PROJECT WITH US?</span></h2>
  </div>
  <div class="abs contact-photo" role="img" aria-label="Laser cutter head cutting sheet metal with orange sparks"></div>
  <form class="abs form-card">
    <h3>Send Us A Message</h3>
    <div class="fields">
      <div class="field">First Name*</div>
      <div class="field">Last Name*</div>
      <div class="field">Email*</div>
      <div class="field">Phone Number*</div>
      <div class="field msg">Message*</div>
    </div>
    <span class="btn">Submit</span>
  </form>
</section>

<footer>
  <div class="abs footer-brand">
    <div class="brand-name">KORVAN <span class="dot" style="width:8px;height:8px"></span></div>
    <div class="brand-tag">PRECISION MACHINISTS</div>
    <p>Leading Experts in CNC Machining, EDM Wire Cutting, and 3D Metal Printing.</p>
    <div class="f-social"><span></span><span></span><span></span><span></span></div>
  </div>
  <div class="abs f-col" style="left:450px">
    <h4>Quick Links</h4>
    <ul><li>Home</li><li>About Us</li><li>EDM Wire Cutting</li><li>CNC Machining</li><li>Laser Marking &amp; Etching</li></ul>
  </div>
  <div class="abs f-col" style="left:655px">
    <h4>Help</h4>
    <ul><li>Help Center</li><li>FAQs</li><li>Privacy policy</li><li>Terms of use Cookie</li><li>settings</li></ul>
  </div>
  <div class="abs f-col f-contact" style="left:839px">
    <h4>Contact Information</h4>
    <ul style="margin-top:14px">
      <li><svg width="8" height="11" viewBox="0 0 8 11"><path d="M4 0a4 4 0 0 1 4 4c0 3-4 7-4 7S0 7 0 4a4 4 0 0 1 4-4z" fill="#23905a"/><circle cx="4" cy="4" r="1.4" fill="#15414a"/></svg><span>1420 Harlow Street<br>Suite 300 Brookfield, VT 05036</span></li>
      <li><svg width="10" height="10" viewBox="0 0 24 24" fill="#23905a"><path d="M6.6 10.8a15.1 15.1 0 0 0 6.6 6.6l2.2-2.2a1 1 0 0 1 1-.25 11.4 11.4 0 0 0 3.6.57 1 1 0 0 1 1 1V20a1 1 0 0 1-1 1A17 17 0 0 1 3 4a1 1 0 0 1 1-1h3.5a1 1 0 0 1 1 1c0 1.25.2 2.45.57 3.57a1 1 0 0 1-.25 1z"/></svg><span>1.800.555.0147</span></li>
      <li><svg width="10" height="8" viewBox="0 0 24 18"><path d="M0 0h24v18H0z" fill="#23905a"/><path d="M0 0l12 9 12-9" stroke="#15414a" stroke-width="2" fill="none"/></svg><span>info@korvansupport.com</span></li>
    </ul>
  </div>
  <div class="abs copyright">© 2024 KORVAN. All rights reserved.</div>
</footer>

</body>
</html>
```